Velcor Prime Brochure for Chemicals Products

We need a bifold A3 brochure for the exhibition.
you can visit our company website (www.velcorprime.com) for more information about our company.
Company logo and color code attached.
The brochure should contain brief introduction of company, industries, product, and contact (address , telephone and email; joral.k@velcorprime.com)

Product Portfolio:
1. Intermediates
2. Plastics
3. Rubber
4. Additive
5. Fiber
Detail of each products portfolio are in the website. we would like to add product detail but you may help to design how to put it beautifully.

Target Market(s)

Our customers are factories in related industry.

Industry/Entity Type

Automotive, Paint, Electrical Appliance, Tyre and footwear, Textile, Animal Feed, Lubricant

Font styles to use
Sans Serif

Requirements
Must have
• Logo, Product Portfolio for different market.
Nice to have
• prefer curve design rather than rectangular

```html
<!DOCTYPE html>
<html lang="en">
<head>
<meta charset="utf-8">
<title>Velcor Prime Brochure</title>
<link rel="stylesheet" href="https://fonts.googleapis.com/css2?family=Rubik:wght@700;800&family=Montserrat:wght@400;500;600&display=swap">
<style>
:root{
  --blue:#1f93d8;
  --blue-deep:#1a6aa6;
  --lime:#b9d632;
  --ink:#3f4448;
  --ink-soft:#6b7075;
  --paper:#ffffff;
  --stage:#f0f0f0;
  --rule:#8a8a8a;
}
*{box-sizing:border-box;margin:0;padding:0}
html,body{width:1200px;height:2207px;overflow:hidden}
body{background:var(--stage);font-family:"Montserrat",sans-serif;color:var(--ink);position:relative}
.masthead-rule{position:absolute;left:0;top:61px;width:876px;height:2px;background:#6d6d6d}
.masthead-name{position:absolute;right:48px;top:44px;font-family:"Montserrat",sans-serif;font-weight:500;font-size:30px;letter-spacing:2px;color:#4a4a4a}
.spread{position:absolute;left:80px;width:1040px;height:735px;display:flex;box-shadow:0 18px 40px rgba(0,0,0,.14)}
.spread--outer{top:190px}
.spread--inner{top:1190px}
.page{position:relative;width:520px;height:735px;background:var(--paper);overflow:hidden}
.page + .page{border-left:1px solid #e4e4e4}
.display{font-family:"Rubik",sans-serif;font-weight:800}
.accent{color:var(--lime)}
/* back cover */
.back-title{position:absolute;left:40px;top:78px;width:440px;font-size:23px;line-height:1.22;color:var(--blue)}
.back-lede{position:absolute;left:40px;top:190px;width:440px;font-size:12px;line-height:1.45;color:var(--ink)}
.contact-title{position:absolute;left:0;width:100%;top:286px;text-align:center;font-size:22px;color:var(--blue)}
.contact-title::after{content:"";display:block;width:100px;height:3px;background:var(--blue);margin:6px auto 0}
.contact-bar{position:absolute;left:40px;top:370px;width:32px;height:230px;background:var(--blue);border-radius:2px}
.contact-bar svg{position:absolute;left:8px;width:16px;height:16px}
.contact-list{position:absolute;left:116px;top:378px;width:380px;list-style:none;font-size:13px;color:var(--ink)}
.contact-list li{position:absolute;left:0;line-height:1.3}
.page-foot{position:absolute;left:0;right:0;bottom:30px;height:20px}
.page-foot .rule{position:absolute;left:0;bottom:9px;width:350px;height:1px;background:var(--rule)}
.page-foot .name{position:absolute;right:22px;bottom:2px;font-size:12px;letter-spacing:1px;color:#555}
/* front cover */
.cover-photo{position:absolute;inset:0;background:
  radial-gradient(circle at 72% 76%,#f6c64a 0,#f07aa8 22%,#9bd4e6 36%,rgba(255,255,255,0) 50%),
  linear-gradient(160deg,#f3f3f3,#e7eef0)}
.cover-shapes{position:absolute;inset:0}
.logo-tile{position:absolute;left:305px;top:10px;width:110px;height:110px;background:#fff;box-shadow:0 2px 6px rgba(0,0,0,.15);display:flex;align-items:center;justify-content:center}
.logo-tile span{font-size:11px;font-weight:600;letter-spacing:.5px;color:var(--blue)}
.cover-title{position:absolute;left:66px;top:222px;font-size:32px;line-height:1.23;color:#fff}
/* inner left */
.section-title{position:absolute;left:40px;font-size:24px;color:var(--blue)}
.section-title::after{content:"";display:block;width:76px;height:3px;background:var(--blue);margin-top:6px}
.who-title{top:62px}
.body-copy{position:absolute;left:40px;width:430px;font-size:12.5px;line-height:1.5;color:var(--ink)}
.copy-a{top:126px}
.copy-b{top:226px}
.pillar{position:absolute;left:52px;width:420px}
.pillar h3{font-size:12.5px;font-weight:600;color:var(--lime);margin-bottom:6px}
.pillar h3::before{content:"•";margin-right:8px}
.pillar p{margin-left:50px;font-size:12.5px;line-height:1.5;color:var(--ink)}
.pillar-1{top:312px}
.pillar-2{top:420px}
.pillar-3{top:510px}
/* inner right */
.products-title{top:62px}
.products-lede{position:absolute;left:40px;top:126px;width:420px;font-size:12.5px;line-height:1.5;color:var(--ink)}
.product{position:absolute;width:140px;text-align:center}
.product .tile{height:150px;border-radius:20px}
.product .label{display:block;margin-top:8px;font-family:"Rubik",sans-serif;font-weight:700;font-size:15px;line-height:1.15;color:var(--blue)}
.p-rubber{left:40px;top:276px}
.p-plastics{left:190px;top:236px}
.p-chemicals{left:340px;top:196px}
.p-fibers{left:40px;top:480px}
.p-additives{left:190px;top:450px}
.p-custom{left:340px;top:420px}
.tile-rubber{background:radial-gradient(circle at 45% 50%,#f4a0c4,#f7d86a 35%,#8fd3e8 55%,#f4f4f4 70%)}
.tile-plastics{background:linear-gradient(150deg,#bfe6ef,#5fb7cf 60%,#d9c3b8)}
.tile-chemicals{background:linear-gradient(160deg,#7a3fb0,#f2c21a 40%,#1fb4a0 65%,#e8186b)}
.tile-fibers{background:linear-gradient(160deg,#2c5ea8,#1c3f80)}
.tile-additives{background:linear-gradient(160deg,#f1f1f1,#cfe9ec 50%,#c89a5c)}
.tile-custom{background:linear-gradient(160deg,#3f6fd0,#9fd0f2 55%,#dbeefa)}
</style>
</head>
<body>
<div class="masthead-rule"></div>
<div class="masthead-name">VELCOR PRIME</div>

<section class="spread spread--outer" aria-label="Outer spread">
  <article class="page back-cover">
    <h2 class="back-title display">Build Trusted Long Term Partnership For Sustainable Growth</h2>
    <p class="back-lede">We strive to lead and sustain excellence. Most importantly, this means an unwaavering commitment and trusted services.</p>
    <h2 class="contact-title display">Contact&nbsp; Us</h2>
    <div class="contact-bar" aria-hidden="true">
      <svg style="top:14px" viewBox="0 0 16 16" fill="#fff"><circle cx="8" cy="5" r="3.5"/><path d="M1 16c0-4 3-6 7-6s7 2 7 6z"/></svg>
      <svg style="top:54px" viewBox="0 0 16 16" fill="#fff"><path d="M8 0a5.5 5.5 0 0 0-5.5 5.5C2.5 10 8 16 8 16s5.5-6 5.5-10.5A5.5 5.5 0 0 0 8 0zm0 8a2.5 2.5 0 1 1 0-5 2.5 2.5 0 0 1 0 5z"/></svg>
      <svg style="top:94px" viewBox="0 0 16 16" fill="#fff"><path d="M4 1l2.5 3.5-1.5 1.8c.8 2 2.6 3.8 4.6 4.6l1.8-1.5L15 12l-1.5 2.5C7 15 1 9 1.5 2.5z"/></svg>
      <svg style="top:134px" viewBox="0 0 16 16" fill="none" stroke="#fff" stroke-width="1.6"><rect x="1" y="3" width="14" height="10"/><path d="M1 3l7 6 7-6M1 13l5-5M15 13l-5-5"/></svg>
      <svg style="top:174px" viewBox="0 0 16 16" fill="none" stroke="#fff" stroke-width="1.5"><circle cx="8" cy="8" r="7"/><path d="M1 8h14M8 1c-3 3-3 11 0 14M8 1c3 3 3 11 0 14"/></svg>
    </div>
    <ul class="contact-list">
      <li style="top:0">Joral Kettisak</li>
      <li style="top:36px">88/14 Meridian Lane (Harbor 7), Harbor Rd.,<br>Eastgate, Riverton 20410</li>
      <li style="top:88px">+66-81-4096271</li>
      <li style="top:128px">joral.k@velcorprime.com</li>
      <li style="top:168px">http://www.velcorprime.com</li>
    </ul>
    <footer class="page-foot"><span class="rule"></span><span class="name">VELCOR PRIME</span></footer>
  </article>

  <article class="page front-cover">
    <div class="cover-photo" role="img" aria-label="Photo of a colourful ball of rubber bands on a white wooden table"></div>
    <svg class="cover-shapes" viewBox="0 0 520 735" preserveAspectRatio="none" aria-hidden="true">
      <defs>
        <linearGradient id="coverBlue" x1="0" y1="0" x2="1" y2="1">
          <stop offset="0" stop-color="#2699de"/>
          <stop offset="1" stop-color="#1a6aa6"/>
        </linearGradient>
      </defs>
      <path d="M0 575 C370 455 480 260 505 0 L520 0 L520 70 C500 310 390 490 0 612 Z" fill="var(--lime)"/>
      <path d="M0 0 H505 C470 250 360 440 0 575 Z" fill="url(#coverBlue)"/>
      <path d="M318 262 C420 235 485 150 505 0 C478 170 420 232 318 262 Z" fill="var(--lime)"/>
    </svg>
    <div class="logo-tile"><span>VELCOR PRIME</span></div>
    <h1 class="cover-title display">The Best<br>Value for<br>Business<br>with <span class="accent">Perfect</span><br><span class="accent">Growth</span></h1>
  </article>
</section>

<section class="spread spread--inner" aria-label="Inner spread">
  <article class="page about">
    <h2 class="section-title who-title display">Who We Are</h2>
    <p class="body-copy copy-a">Established in 2004, we started our business supplying recycle plastics and consumer goods. In 2011, we transformed the business and active in distribution and sales of chemicals and polymers. Today our business covers upstream and downstream market as well as international trading.</p>
    <p class="body-copy copy-b">We are deeply dedicated to the long-term growth and success of our partners and our people. We are dedicated to producing measured value and results.</p>
    <div class="pillar pillar-1">
      <h3>Business &amp; Market Strategy</h3>
      <p>Develop and promote new product from suppliers globally. Bring benefit to our clients through our network and expertise. Deliver what customer's needs.</p>
    </div>
    <div class="pillar pillar-2">
      <h3>Excellence In Services</h3>
      <p>Beyond logistics provider. When you get one of us, you get all of us. We bring innovative solutions and reliable advice.</p>
    </div>
    <div class="pillar pillar-3">
      <h3>Our People Make Difference</h3>
      <p>Well committed and qualified with years of experience team. We serve you with our passion.</p>
    </div>
  </article>

  <article class="page products">
    <h2 class="section-title products-title display">Our Products</h2>
    <p class="products-lede">From upstream to downstream, our portfolio covers various polymer related products including customs formulation solutions</p>
    <figure class="product p-rubber"><div class="tile tile-rubber" role="img" aria-label="Photo of a ball of rubber bands"></div><figcaption class="label">Rubber</figcaption></figure>
    <figure class="product p-plastics"><div class="tile tile-plastics" role="img" aria-label="Photo of a hand holding blue plastic pellets"></div><figcaption class="label">Plastics</figcaption></figure>
    <figure class="product p-chemicals"><div class="tile tile-chemicals" role="img" aria-label="Photo of open paint cans in bright colours"></div><figcaption class="label">Chemicals</figcaption></figure>
    <figure class="product p-fibers"><div class="tile tile-fibers" role="img" aria-label="Photo of blue yarn spools"></div><figcaption class="label">Fibers</figcaption></figure>
    <figure class="product p-additives"><div class="tile tile-additives" role="img" aria-label="Photo of a liquid being poured into a bowl of powder"></div><figcaption class="label">Additives</figcaption></figure>
    <figure class="product p-custom"><div class="tile tile-custom" role="img" aria-label="Photo of laboratory glassware with a pipette"></div><figcaption class="label">Customs<br>Formulation</figcaption></figure>
    <footer class="page-foot"><span class="rule"></span><span class="name">VELCOR PRIME</span></footer>
  </article>
</section>
</body>
</html>
```